Visitenkarten-Design für Süßigkeiten-Onlineshop
Zielgruppe
Ich werde einen Onlineshop betreiben und Süßigkeiten aus aller Welt verkaufen.
Aufgabenstellung
Mein Logo sollte drauf sein. Die Visitenkarte kann auch bisschen stylischer gestaltet werden. Aber da lasse ich mich auch gerne überraschen.
Man könnte vielleicht noch den Slogan- Süßigkeiten aus aller Welt-
Mein Name sollte drauf stehen,
Jonas Brettel
Lindauer Weg 14
41562 Dormagen
E-Mail info@zuckerfuchs-shop.de
Instagram @zuckerfuchs.de
Facebook Zuckerfuchs
Tic Toc @zuckerfuhcs.de

```html
<!DOCTYPE html>
<html lang="de">
<head>
<meta charset="utf-8">
<title>Zuckerfuchs – Visitenkarten</title>
<link rel="stylesheet" href="https://fonts.googleapis.com/css2?family=Open+Sans:wght@400;600&display=swap">
<style>
  :root {
    --canvas: #ffffff;
    --stage-top: #d2d2d2;
    --stage-bottom: #f1f1f1;
    --teal: #5fb3b5;
    --teal-text: #3fa7ab;
    --teal-pale: #d4ecec;
    --teal-soft: #a9d6d7;
    --ink: #2b2f33;
    --card-white: #f7f7f7;
  }
  * { box-sizing: border-box; margin: 0; padding: 0; }
  html, body { width: 1200px; height: 3000px; overflow: hidden; background: var(--canvas); }
  body { font-family: "Open Sans", sans-serif; }

  .stage {
    position: absolute; left: 0; width: 1200px; height: 968px;
    background: linear-gradient(180deg, var(--stage-top), var(--stage-bottom));
    display: flex; align-items: center; justify-content: center; gap: 40px;
  }
  .stage--one { top: 0; }
  .stage--two { top: 1016px; }
  .stage--three { top: 2032px; }

  .card {
    position: relative; width: 540px; height: 350px; overflow: hidden;
    box-shadow: 0 10px 28px rgba(0,0,0,.14);
  }

  /* Front */
  .card--front { background: var(--teal-pale); }
  .card__rays {
    position: absolute; inset: 0;
    background: radial-gradient(ellipse at 45% 25%, var(--teal-pale) 0%, var(--teal-soft) 60%, var(--teal-pale) 100%);
    opacity: .8;
  }
  .front__brand {
    position: absolute; left: 0; right: 0; top: 70px;
    display: flex; flex-direction: column; align-items: center; gap: 18px;
  }
  .brand__dot { width: 110px; height: 110px; border-radius: 50%; background: var(--teal); }
  .brand__name {
    font-size: 40px; font-weight: 400; letter-spacing: 4px; color: var(--ink);
    text-transform: uppercase;
  }
  .card__band {
    position: absolute; left: 0; right: 0; bottom: 0; height: 48px;
    background: var(--teal); color: #fff;
    display: flex; align-items: center; justify-content: center;
    font-size: 20px; letter-spacing: 3px;
  }

  /* Back */
  .card--back { background: var(--card-white); }
  .back__identity {
    position: absolute; left: 40px; top: 38px; width: 240px;
    display: flex; flex-direction: column; align-items: center;
  }
  .back__dot { width: 64px; height: 64px; border-radius: 50%; background: var(--teal); margin-bottom: 10px; }
  .back__brand { font-size: 20px; letter-spacing: 2px; color: var(--ink); text-transform: uppercase; margin-bottom: 10px; }
  .back__name { font-size: 20px; font-weight: 600; color: var(--teal-text); line-height: 1.1; }
  .back__role { font-size: 16px; color: var(--teal-text); }
  .back__address {
    position: absolute; left: 40px; right: 20px; bottom: 64px;
    font-size: 15px; line-height: 1.4; color: var(--teal-text); white-space: nowrap;
  }
  .back__social {
    position: absolute; left: 300px; top: 48px; list-style: none;
    display: flex; flex-direction: column; gap: 22px;
  }
  .social__item { display: flex; align-items: center; gap: 12px; font-size: 15px; color: var(--teal-text); }
  .social__mark { width: 26px; height: 26px; border-radius: 50%; border: 2px solid var(--teal); }
</style>
</head>
<body>

<section class="stage stage--one">
  <article class="card card--back">
    <div class="back__identity">
      <span class="back__dot"></span>
      <span class="back__brand">Zuckerfuchs</span>
      <span class="back__name">Jonas Brettel</span>
      <span class="back__role">owner</span>
    </div>
    <ul class="back__social">
      <li class="social__item"><span class="social__mark"></span>@zuckerfuchs.de</li>
      <li class="social__item"><span class="social__mark"></span>Zuckerfuchs</li>
      <li class="social__item"><span class="social__mark"></span>@zuckerfuchs.de</li>
    </ul>
    <p class="back__address">Lindauer Weg 14 41562 Lindenbrück<br>Tel.Nr.: 015298765432 | info@zuckerfuchs-shop.de</p>
    <div class="card__band">24/7 täglich shoppen</div>
  </article>
  <article class="card card--front">
    <div class="card__rays" role="img" aria-label="Geschwungenes Strahlenmuster in Türkistönen"></div>
    <div class="front__brand"><span class="brand__dot"></span><span class="brand__name">Zuckerfuchs</span></div>
    <div class="card__band">Süßigkeiten aus aller Welt!</div>
  </article>
</section>

<section class="stage stage--two">
  <article class="card card--front">
    <div class="card__rays" role="img" aria-label="Geschwungenes Strahlenmuster in Türkistönen"></div>
    <div class="front__brand"><span class="brand__dot"></span><span class="brand__name">Zuckerfuchs</span></div>
    <div class="card__band">Süßigkeiten aus aller Welt!</div>
  </article>
  <article class="card card--back">
    <div class="back__identity">
      <span class="back__dot"></span>
      <span class="back__brand">Zuckerfuchs</span>
      <span class="back__name">Jonas Brettel</span>
      <span class="back__role">owner</span>
    </div>
    <ul class="back__social">
      <li class="social__item"><span class="social__mark"></span>@zuckerfuchs.de</li>
      <li class="social__item"><span class="social__mark"></span>Zuckerfuchs</li>
      <li class="social__item"><span class="social__mark"></span>@zuckerfuchs.de</li>
    </ul>
    <p class="back__address">Lindauer Weg 14 41562 Lindenbrück<br>Tel.Nr.: 015298765432 | info@zuckerfuchs-shop.de</p>
    <div class="card__band">24/7 täglich shoppen</div>
  </article>
</section>

<section class="stage stage--three">
  <article class="card card--front">
    <div class="card__rays" role="img" aria-label="Geschwungenes Strahlenmuster in Türkistönen"></div>
    <div class="front__brand"><span class="brand__dot"></span><span class="brand__name">Zuckerfuchs</span></div>
    <div class="card__band">Süßigkeiten aus aller Welt!</div>
  </article>
  <article class="card card--front">
    <div class="card__rays" role="img" aria-label="Geschwungenes Strahlenmuster in Türkistönen"></div>
    <div class="front__brand"><span class="brand__dot"></span><span class="brand__name">Zuckerfuchs</span></div>
    <div class="card__band">Süßigkeiten aus aller Welt!</div>
  </article>
</section>

</body>
</html>
```